Flyer Design for International Business Consultant

We need an advertisement to help build the profile of Miles Haversham, Senior Consultant and Director at 'ORB Advisory Group'.

What we want to promote:
Our Senior Consultant and Director, Miles Haversham as expert on all matters China related.

Who are we promoting to:
Industry associations and networking groups.

Why:
Many organisations are interested in reaching the Chinese market, however don't know who to go to or who to trust. With many consultants out there trying to claim they offer a similar service, ORB would like to promote Miles as a genuine expert in the field and the 'go to' person on all things China business related. To do this, we are in the process of building Miles's national and international profile, which includes advertising Miles expertise to industry associations and networking groups so that they consider booking Miles as a key note speaker at conferences. We know that our target audience are more inclined to seek the advice of someone they have seen speak at a conference than to find someone in the Golden listings or via findly search.

A Bit about Miles Haversham:

Miles Haversham has lived, worked and studied in China for extended periods, speaks and writes fluently in Chinese, was formerly a Member of the Tasmanian Government Trade Outreach Advisory Panel, is a member of the Institute of Global Commerce Studies and is a member of the Pacific Asia Enterprise Forum to name a few. To add to his credentials, Miles has by invitation lectured for 5 consecutive years in Management and Economics at Masters Level to students at Kowloon Harbour College.

Miles’s qualifications include: Bachelor of Arts (Asian Studies), Bachelor of Business (Applied Economics – International Trade), Master of Business in Applied Economics (International Business) and currently completing a Doctor of Business Administration (International Business Management) which has an economics focus and researches the export of Australian professional services to China.

Miles has been the Principal Consultant for a number of ORB’s clients including the recent assignment commissioned by Victorian based company BRN Freightways, who have benefited from a $40 million deal with Eastern Plains Locomotive (EPL). This project has also resulted in EPL, China’s largest train manufacturer decision to set up offices in Victoria.

Miles is an expert in Australia/China Business relations and has been paramount to the success of numerous international business transactions. As mentioned, Miles is not only fluent in spoken and written Mandarin, but is also a bi-cultural expert (meaning he knows both Australian and Chinese) cultures. From Australian and Chinese history, art, food and more, Miles Haversham provides his clients with more than translation services.

A Bit about ORB Advisory Group:

Run by experienced business executives with over 20 years’ experience in the Chinese and Australian markets, ORB brings a un-paralleled level of knowledge and expertise that enables cooperative business relations to develop between international organisations despite the language and cultural differences. They are a bi-lingual and bi-cultural international business consultancy that specialise in managing cross-border business involving China.

ORB has expertise in all facets of business management and has worked with a range of companies and organisations to develop and implement strategic business solutions to set direction, improve performance and maximise returns to stakeholders. ORB has particular expertise in economic and market analysis and specialises in project management of large and complex projects, strategic procurement, market research and market development strategies. Combined with their cultural and language skills, ORB provides a unique and high value contribution to international projects.

Good afternoon designers

Thank you for your submissions so far.  We are happy with some of the designs that have come in, however, many of you have produced flyers that have too much information in it.  We are looking for something more concise that does not appear to be either a copy of information I have posted in this brief or a fancy looking resume for Miles Haversham. 

Please remember, we are communicating to event co-ordinators who are looking to appoint guest speakers at an upcoming conference.  They want someone who is going to discuss some of the 'hot topics' their audience are interested in, someone who is experienced in the topic and someone who is interesting. We need to communicate all of this in a concise, and creative way so that we can make Miles Haversham stand out above the rest.

Dear Designers

Thank you all very much for your submissions.  We appreciate you taking the time to compose a flyer for our organisation. 

Regards
Rosa

Dear Designers

Regards
Rosa

Target Market(s)

Event/conference managers or coordinators

Industry/Entity Type

Business Management

Requirements
Must have
• Must have the ORB Logo on it (red, white and black). The ad will be in the form of an electronic flyer to be embedded in an email that will be sent on to relevant contacts in our database.

```html
<!DOCTYPE html>
<html lang="en">
<head>
<meta charset="utf-8">
<title>Miles Haversham – ORB Advisory Group</title>
<link href="https://fonts.googleapis.com/css2?family=Arimo:wght@400;700&family=Cormorant+Garamond:wght@500&family=Great+Vibes&display=swap" rel="stylesheet">
<style>
  :root {
    --brand-red: #e41e26;
    --ink: #111111;
    --body-ink: #1a1a1a;
    --soft-ink: #3a3a3a;
    --icon-grey: #d9d9d9;
    --paper: #ffffff;
  }
  html, body { margin: 0; padding: 0; overflow: hidden; background: var(--paper); }
  .flyer {
    position: relative; width: 848px; height: 1200px; overflow: hidden;
    background: var(--paper); color: var(--body-ink);
    font-family: "Arimo", Arial, sans-serif;
  }
  .brand { position: absolute; left: 102px; top: 68px; display: flex; align-items: center; gap: 12px; }
  .brand-mark { width: 94px; height: 94px; background: var(--brand-red); }
  .brand-name { font-weight: 700; color: var(--ink); line-height: 1; }
  .brand-name .big { display: block; font-size: 66px; letter-spacing: -1px; }
  .brand-name .small { display: block; font-size: 17px; margin-top: 4px; letter-spacing: 0.2px; }

  .headline { position: absolute; right: 112px; top: 150px; white-space: nowrap; color: var(--ink); }
  .headline .serif { font-family: "Cormorant Garamond", Georgia, serif; font-size: 58px; }
  .headline .script { font-family: "Great Vibes", cursive; font-size: 62px; }

  .label { position: absolute; font-weight: 700; font-size: 14.5px; color: var(--ink); margin: 0; }
  .label.about-person { left: 105px; top: 213px; }
  .label.about-company { left: 438px; top: 667px; text-transform: uppercase; }

  .intro { position: absolute; left: 105px; top: 246px; width: 630px; margin: 0;
    font-size: 17.2px; line-height: 20px; text-align: justify; }

  .section-title { position: absolute; left: 103px; top: 396px; margin: 0; white-space: nowrap; color: var(--ink); font-weight: 400; }
  .section-title .script { font-family: "Great Vibes", cursive; font-size: 62px; }
  .section-title .serif { font-family: "Cormorant Garamond", Georgia, serif; font-size: 29px; }

  .column { position: absolute; font-size: 14.6px; line-height: 18.5px; }
  .column p { margin: 0 0 18.5px; }
  .column.left { left: 108px; top: 464px; width: 300px; }
  .column.right { left: 438px; top: 464px; width: 300px; }
  .end-mark { display: inline-block; width: 7px; height: 7px; background: var(--brand-red); margin-left: 6px; }

  .company { position: absolute; left: 438px; top: 700px; width: 320px;
    font-size: 13.4px; line-height: 17.1px; color: var(--soft-ink); }
  .company p { margin: 0 0 17px; }

  .contact { position: absolute; right: 445px; top: 900px; text-align: right; }
  .contact-title { margin: 0; display: flex; align-items: center; justify-content: flex-end; gap: 8px; }
  .contact-title .bullet { width: 10px; height: 10px; background: var(--brand-red); }
  .contact-title .script { font-family: "Great Vibes", cursive; font-size: 44px; font-weight: 400; color: var(--ink); line-height: 1; }
  .contact address { font-style: normal; font-size: 12.6px; line-height: 15.4px; margin-top: 6px; color: var(--ink); }
  .social { display: flex; justify-content: flex-end; gap: 6px; margin-top: 12px; }
  .social span { width: 30px; height: 30px; background: var(--icon-grey); border-radius: 3px; }

  .footer-band { position: absolute; left: 0; bottom: 0; width: 848px; height: 79px; background: var(--brand-red); }
</style>
</head>
<body>
<div class="flyer">
  <div class="brand">
    <div class="brand-mark"></div>
    <div class="brand-name"><span class="big">ORB</span><span class="small">ADVISORY GROUP</span></div>
  </div>

  <h1 class="headline"><span class="serif">Miles </span><span class="script">Haversham,</span></h1>

  <h2 class="label about-person">A Bit about Miles Haversham:</h2>
  <p class="intro">Miles Haversham has lived, worked and studied in China for extended periods, speaks and writes fluently in Chinese, was formerly a Member of the Tasmanian Government Trade Outreach Advisory Panel, is a member of the Institute of Global Commerce Studies and is a member of the Pacific Asia Enterprise Forum to name a few. To add to his credentials, Miles has by invitation lectured for 5 consecutive years in Management and Economics at Masters Level to students at Kowloon Harbour College.</p>

  <h2 class="section-title"><span class="script">Miles’s </span><span class="serif">qualifications include:</span></h2>

  <div class="column left">
    <p>Bachelor of Arts (Asian Studies), Bachelor of Business (Applied Economics – International Trade), Master of Business in Applied Economics (International Business) and currently completing a Doctor of Business Administration (International Business Management) which has an economics focus and researches the export of Australian professional services to China.</p>
    <p>Miles has been the Principal Consultant for a number of ORB’s clients including the recent assignment commissioned by Victorian based company BRN Freightways, who have benefited from a $40 million deal with Eastern Plains Locomotive (EPL). This project has also resulted in EPL, China’s largest train manufacturer decision to set up offices in Victoria.</p>
    <p>Miles is an expert in Australia/China Business relations and has been</p>
  </div>

  <div class="column right">
    <p>paramount to the success of numerous international business transactions. As mentioned, Miles is not only fluent in spoken and written Mandarin, but is also a bi-cultural expert (meaning he knows both Australian and Chinese) cultures. From Australian and Chinese history, art, food and more, Miles Haversham provides his clients with more than translation services<span class="end-mark"></span></p>
  </div>

  <h2 class="label about-company">A Bit about ORB Advisory Group:</h2>
  <div class="company">
    <p>Run by experienced business executives with over 20 years’ experience in the Chinese and Australian markets, ORB brings a un-paralleled level of knowledge and expertise that enables cooperative business relations to develop between international organisations despite the language and cultural differences. They are a bi-lingual and bi-cultural international business consultancy that specialise in managing cross-border business involving China.</p>
    <p>ORB has expertise in all facets of business management and has worked with a range of companies and organisations to develop and implement strategic business solutions to set direction, improve performance and maximise returns to stakeholders. ORB has particular expertise in economic and market analysis and specialises in project management of large and complex projects, strategic procurement, market research and market development strategies. Combined with their cultural and language skills, ORB provides a unique and high value contribution to international projects.</p>
  </div>

  <div class="contact">
    <h2 class="contact-title"><span class="bullet"></span><span class="script">Contact Miles</span></h2>
    <address>
      14 Larkspur Lane, Kew Heights, Victoria, 3188.<br>
      TEL : (61) 03 5550 1234<br>
      Mob : (61) 0400 555 017<br>
      miles@orbadvisory.com.au<br>
      www.orbadvisory.com.au
    </address>
    <div class="social" aria-label="Social links"><span></span><span></span><span></span></div>
  </div>

  <div class="footer-band"></div>
</div>
</body>
</html>
```